KVO - Redesign (PSD Files Only)

Requirements for the site:

1. We need our logo recreated, please use the same design and change colors to work on a white background

2. The site is a "Wizard" based site, that takes the customer through the process of creating a unique web presence that suits there needs

3.Colors Needed - Main "Dark Blue" Secondary = "Dark Grey" -Other = "Light Grey and White"

4.We need a CRISP CLEAN DESIGN, simple design

5.Wireframes are a general layout and may be modified by you to enhance the design

6. We want a complete web 5.0 look with big buttons and text boxes

7.The more personality the better

8. Current Site brightmorrowco.example

9.See attachments for wireframes

10. Designer should deliver PSD files, no coding is required

11. The portfolio wireframe, should look like the design of the pixelharbor portfolio template
Updates

KEEP IT SIMPLE.,.....

We like the quillframe scaffold style of designs

```html
<!DOCTYPE html>
<html lang="en">
<head>
<meta charset="utf-8">
<title>KVO – Choose a Project Manager</title>
<link href="https://fonts.googleapis.com/css2?family=Dosis:wght@500;600;700&family=Open+Sans:ital,wght@0,400;0,600;0,700;1,400&display=swap" rel="stylesheet">
<style>
:root{
  --navy:#04355f;
  --navy-deep:#022444;
  --blue-mid:#0a4d80;
  --ink-dark:#1d1d1d;
  --ink-darker:#161616;
  --grey-bg:#d3d3d3;
  --grey-line:#e3e3e3;
  --white:#ffffff;
  --orange-top:#ff9a2e;
  --orange-bot:#ff6a00;
  --muted:#a9a9a9;
}
*{box-sizing:border-box;margin:0;padding:0}
html,body{width:1200px;height:1043px;overflow:hidden}
body{position:relative;background:var(--grey-bg);font-family:"Open Sans",sans-serif;color:var(--navy)}
.abs{position:absolute}
.header{left:0;top:0;width:1200px;height:173px;background:radial-gradient(ellipse at 50% 100%,#0a5a8e 0%,var(--navy) 45%,var(--navy-deep) 100%)}
.header-topband{left:0;top:0;width:1200px;height:23px;background:var(--ink-dark)}
.navbar{left:129px;top:0;width:942px;height:46px;background:var(--ink-dark)}
.brand{left:150px;top:9px;font-family:"Dosis",sans-serif;font-weight:700;font-size:20px;color:var(--white);letter-spacing:1px}
.nav a{position:absolute;top:0;height:46px;line-height:46px;font-family:"Dosis",sans-serif;font-weight:500;font-size:21px;color:var(--white);text-decoration:none;padding:0 13px}
.nav a.active{background:var(--navy)}
.social-dot{width:26px;height:26px;border-radius:50%;background:var(--white)}
.phone{font-family:"Dosis",sans-serif;font-weight:500;color:var(--white);display:flex;align-items:center;gap:5px}
.step{left:0;width:1200px;text-align:center;color:var(--white)}
.step-label{top:70px;font-size:15px}
.step-title{top:88px;font-family:"Dosis",sans-serif;font-weight:700;font-size:35px;display:flex;justify-content:center;align-items:center;gap:16px}
.dots{font-size:20px;letter-spacing:1px;opacity:.9;position:relative;top:-4px}
.notch{left:588px;top:161px;width:0;height:0;border-left:12px solid transparent;border-right:12px solid transparent;border-bottom:12px solid var(--white)}
.panel{left:129px;top:173px;width:942px;height:651px;background:var(--white);border:1px solid #cfcfcf;border-top:none}
.crumbs{left:171px;top:193px;font-size:13px;display:flex;gap:9px;align-items:center}
.crumbs .sep{font-weight:700;font-size:14px}
.crumbs .current{color:var(--muted)}
.rule{left:130px;top:226px;width:940px;height:1px;background:var(--grey-line)}
.gauge{left:800px;top:179px}
.pm-name{top:280px;font-weight:700;font-size:15px}
.pm-name span{font-weight:400;font-style:italic;font-size:12px;color:var(--muted)}
.video{top:306px;width:272px;height:221px;background:#000}
.video-screen{position:absolute;left:0;top:0;width:272px;height:186px;background:radial-gradient(circle at 50% 45%,#0b4a7c 0%,#063868 45%,#032448 100%);display:flex;align-items:center;justify-content:center;flex-direction:column;color:var(--white)}
.video-screen b{font-family:"Dosis",sans-serif;font-size:30px;letter-spacing:1px}
.video-screen small{font-size:8px;margin-top:2px}
.controls{position:absolute;left:0;top:186px;width:272px;height:35px}
.check{top:541px;width:26px;height:25px;border:1px solid #c9c9c9;border-radius:2px;background:var(--white)}
.check.on{border-color:var(--navy)}
.cta{background:linear-gradient(var(--orange-top),var(--orange-bot));color:var(--white);font-family:"Dosis",sans-serif;font-weight:700;font-size:27px;display:flex;align-items:center;justify-content:center;border:1px solid #f07a10}
.cta-main{left:478px;top:596px;width:244px;height:54px}
.cta-note{left:479px;top:654px;font-size:16px;line-height:19px}
.info{left:154px;top:733px;width:891px;height:71px;background:var(--navy);color:var(--white);font-style:italic;font-size:15.5px;line-height:18px;padding:16px 0 0 55px}
.info b{font-style:normal}
.info-icon{left:170px;top:750px}
.footer{left:0;top:824px;width:1200px;height:219px;background:var(--ink-dark)}
.footer-strip{left:285px;top:948px;width:793px;height:53px;background:var(--ink-darker)}
.footer-text{left:129px;color:var(--white);font-size:13px}
.footer-links{top:867px;display:flex;gap:8px}
.f-social{width:38px;height:38px;border-radius:50%;background:var(--white);top:863px}
.badge{left:129px;top:948px;width:156px;height:53px;background:var(--white);display:flex}
.badge i{width:54px;height:53px;background:#3b6fd1}
.cta-foot{left:828px;top:862px;width:243px;height:55px}
</style>
</head>
<body>
<div class="abs header"></div>
<div class="abs header-topband"></div>
<div class="abs navbar"></div>
<div class="abs brand">KVO</div>
<nav class="nav">
  <a class="abs" style="left:222px" href="#">Home</a>
  <a class="abs active" style="left:295px" href="#">About Us</a>
  <a class="abs" style="left:392px" href="#">Portfolio</a>
  <a class="abs" style="left:477px" href="#">Contact Us</a>
</nav>
<div class="abs social-dot" style="left:704px;top:10px"></div>
<div class="abs social-dot" style="left:738px;top:10px"></div>
<div class="abs social-dot" style="left:771px;top:10px"></div>
<div class="abs social-dot" style="left:804px;top:10px"></div>
<div class="abs phone" style="left:884px;top:7px;font-size:25px">
  <svg width="14" height="18" viewBox="0 0 14 18"><path d="M3 1l3 4-2 2c1 3 3 5 5 6l2-2 3 3-2 3C6 16 1 10 1 3z" fill="#fff"/></svg>1800-555-0142
</div>

<div class="abs step step-label">STEP 4</div>
<div class="abs step step-title"><span class="dots">••••••••</span>Choose a Project Manager<span class="dots">••••••••</span></div>
<div class="abs notch"></div>

<div class="abs panel"></div>
<div class="abs crumbs"><span>Level 1</span><span class="sep">»</span><span>Level 2</span><span class="sep">»</span><span>Level 3</span><span class="sep">»</span><span class="current">Level 4</span></div>
<div class="abs rule"></div>
<svg class="abs gauge" width="86" height="86" viewBox="0 0 86 86">
  <circle cx="43" cy="43" r="42" fill="#fff"/>
  <circle cx="43" cy="43" r="31" fill="none" stroke="#e6e6e6" stroke-width="13"/>
  <path d="M43 12 A31 31 0 0 0 12 43" fill="none" stroke="#04355f" stroke-width="13"/>
  <path d="M43 24 L45 43 L41 43 Z" fill="#1d1d1d"/>
  <circle cx="43" cy="43" r="3.5" fill="#1d1d1d"/><circle cx="43" cy="43" r="1.6" fill="#8fb3d9"/>
</svg>

<div class="abs pm-name" style="left:171px">Marcus Hale <span>- Project Manager</span></div>
<div class="abs pm-name" style="left:463px">Marcus Hale <span>- Project Manager</span></div>
<div class="abs pm-name" style="left:754px">Marcus Hale <span>- Project Manager</span></div>

<div class="abs video" style="left:171px">
  <div class="video-screen" role="img" aria-label="Project manager introduction video"><b>KVO</b><small>Kestrel Vale Online</small></div>
  <svg class="controls" viewBox="0 0 272 35"><circle cx="15" cy="18" r="7" fill="#fff"/><path d="M13 14l5 4-5 4z" fill="#000"/><path d="M29 15h3l4-3v12l-4-3h-3z" fill="#fff"/><path d="M39 14q3 4 0 8M42 12q5 6 0 12" stroke="#fff" fill="none" stroke-width="1.5"/><path d="M58 18h48" stroke="#fff" stroke-width="1.5"/><path d="M98 14v8" stroke="#fff" stroke-width="2"/><text x="113" y="22" fill="#fff" font-size="10.5" font-family="Open Sans,sans-serif">2:15 - 4:00</text><circle cx="232" cy="18" r="5" fill="none" stroke="#fff" stroke-width="3"/><path d="M250 11h4M250 11v4M264 11h-4M264 11v4M250 25h4M250 25v-4M264 25h-4M264 25v-4" stroke="#fff" stroke-width="2"/></svg>
</div>
<div class="abs video" style="left:463px">
  <div class="video-screen" role="img" aria-label="Project manager introduction video"><b>KVO</b><small>Kestrel Vale Online</small></div>
  <svg class="controls" viewBox="0 0 272 35"><circle cx="15" cy="18" r="7" fill="#fff"/><path d="M13 14l5 4-5 4z" fill="#000"/><path d="M29 15h3l4-3v12l-4-3h-3z" fill="#fff"/><path d="M39 14q3 4 0 8M42 12q5 6 0 12" stroke="#fff" fill="none" stroke-width="1.5"/><path d="M58 18h48" stroke="#fff" stroke-width="1.5"/><path d="M98 14v8" stroke="#fff" stroke-width="2"/><text x="113" y="22" fill="#fff" font-size="10.5" font-family="Open Sans,sans-serif">2:15 - 4:00</text><circle cx="232" cy="18" r="5" fill="none" stroke="#fff" stroke-width="3"/><path d="M250 11h4M250 11v4M264 11h-4M264 11v4M250 25h4M250 25v-4M264 25h-4M264 25v-4" stroke="#fff" stroke-width="2"/></svg>
</div>
<div class="abs video" style="left:754px">
  <div class="video-screen" role="img" aria-label="Project manager introduction video"><b>KVO</b><small>Kestrel Vale Online</small></div>
  <svg class="controls" viewBox="0 0 272 35"><circle cx="15" cy="18" r="7" fill="#fff"/><path d="M13 14l5 4-5 4z" fill="#000"/><path d="M29 15h3l4-3v12l-4-3h-3z" fill="#fff"/><path d="M39 14q3 4 0 8M42 12q5 6 0 12" stroke="#fff" fill="none" stroke-width="1.5"/><path d="M58 18h48" stroke="#fff" stroke-width="1.5"/><path d="M98 14v8" stroke="#fff" stroke-width="2"/><text x="113" y="22" fill="#fff" font-size="10.5" font-family="Open Sans,sans-serif">2:15 - 4:00</text><circle cx="232" cy="18" r="5" fill="none" stroke="#fff" stroke-width="3"/><path d="M250 11h4M250 11v4M264 11h-4M264 11v4M250 25h4M250 25v-4M264 25h-4M264 25v-4" stroke="#fff" stroke-width="2"/></svg>
</div>

<div class="abs check on" style="left:282px"><svg width="24" height="23" viewBox="0 0 24 23"><path d="M5 12l5 5 9-11" fill="none" stroke="#04355f" stroke-width="2.6"/></svg></div>
<div class="abs check" style="left:574px"></div>
<div class="abs check" style="left:865px"></div>

<div class="abs cta cta-main">Request Consultant</div>
<div class="abs cta-note">Our web professionals will contact<br>you to discuss your project</div>

<div class="abs info">All project managers are employeed by <b>KVO</b> and can be changerd at your request. We only employee <b>US</b> project manager.<br>Each project has a single point of contact with expert advise from our marketing coaches.</div>
<svg class="abs info-icon" width="29" height="29" viewBox="0 0 29 29"><circle cx="14.5" cy="14.5" r="14" fill="#fff"/><circle cx="16" cy="8" r="2.2" fill="#04355f"/><path d="M13 12h4l-2 10h-3" fill="none" stroke="#04355f" stroke-width="2.6"/></svg>

<div class="abs footer"></div>
<div class="abs footer-strip"></div>
<div class="abs footer-text footer-links"><span>Home</span><span>.</span><span>About Us</span><span>.</span><span>Portfolio</span><span>.</span><span>Contact Us</span></div>
<div class="abs footer-text" style="top:886px">Copyright © 2014 Kestrel Vale Online - All Right Reserved</div>
<div class="abs footer-text" style="top:905px">www.brightmorrowco.example</div>
<div class="abs f-social" style="left:498px"></div>
<div class="abs f-social" style="left:544px"></div>
<div class="abs f-social" style="left:588px"></div>
<div class="abs f-social" style="left:635px"></div>
<div class="abs phone" style="left:498px;top:906px;font-size:27px">
  <svg width="15" height="20" viewBox="0 0 14 18"><path d="M3 1l3 4-2 2c1 3 3 5 5 6l2-2 3 3-2 3C6 16 1 10 1 3z" fill="#fff"/></svg>1800-555-0142
</div>
<div class="abs cta cta-foot">Request Consultant</div>
<div class="abs badge" role="img" aria-label="Partner badge"><i></i></div>
</body>
</html>
```